Velmont Systems Business Card

Utilize the newly designed logo to create a polished, professional 2-sided business card for this IT Services company.

Target Market(s)

IT Professionals many in the telecommunications and medical industries.

Industry/Entity Type

Business

Requirements
Must have
• Use of new logo, identified color palette and font: Albertus MT Std Regular.

```html
<!DOCTYPE html>
<html lang="en">
<head>
<meta charset="utf-8">
<title>Velmont Systems Business Card</title>
<link rel="stylesheet" href="https://fonts.googleapis.com/css2?family=Marcellus&display=swap">
<style>
  :root {
    --backdrop: #e4e6ea;
    --card-white: #f1f1f2;
    --brand-navy: #1e3a93;
    --brand-navy-deep: #172f7c;
    --brand-sky: #5d92d8;
    --ink-light: #ffffff;
  }
  * { margin: 0; padding: 0; box-sizing: border-box; }
  html, body {
    width: 1200px;
    height: 1000px;
    overflow: hidden;
    background: var(--backdrop);
    font-family: "Marcellus", serif;
  }
  .sheet {
    width: 1200px;
    height: 1000px;
    display: flex;
    align-items: center;
    justify-content: center;
    gap: 60px;
  }
  .card {
    position: relative;
    width: 510px;
    height: 292px;
    background: linear-gradient(180deg, #f6f6f7 0%, var(--card-white) 100%);
    box-shadow: 0 6px 18px rgba(0,0,0,0.18);
    overflow: hidden;
  }

  /* Front */
  .card--front .band {
    position: absolute;
    left: 0; right: 0;
    background: linear-gradient(90deg, var(--brand-navy-deep), var(--brand-navy));
  }
  .card--front .band--top { top: 0; height: 14px; }
  .card--front .band--bottom { bottom: 0; height: 20px; }
  .brand {
    position: absolute;
    left: 0; right: 0;
    display: flex;
    flex-direction: column;
    align-items: center;
    gap: 14px;
  }
  .card--front .brand { top: 68px; }
  .brand-dot {
    width: 78px;
    height: 78px;
    border-radius: 50%;
    background: var(--brand-sky);
  }
  .brand-name {
    color: var(--brand-navy);
    font-size: 24px;
    letter-spacing: 1.5px;
    text-transform: uppercase;
  }

  /* Back */
  .card--back .brand { top: 42px; }
  .card--back .brand-dot { width: 66px; height: 66px; }
  .card--back .brand-name { font-size: 21px; }
  .info-band {
    position: absolute;
    left: 0; right: 0; bottom: 0;
    height: 104px;
    background: linear-gradient(90deg, var(--brand-navy-deep), var(--brand-navy));
    color: var(--ink-light);
    display: flex;
    justify-content: space-between;
    padding: 18px 22px 16px 24px;
  }
  .person-name {
    font-size: 19px;
    letter-spacing: 0.5px;
  }
  .person-role {
    font-size: 10px;
    margin-top: 6px;
    letter-spacing: 0.5px;
  }
  .contact {
    align-self: flex-end;
    font-size: 11px;
    line-height: 1.45;
    text-align: left;
  }
</style>
</head>
<body>
  <main class="sheet">
    <section class="card card--front" aria-label="Business card front">
      <div class="band band--top"></div>
      <div class="brand">
        <div class="brand-dot"></div>
        <div class="brand-name">Velmont Systems</div>
      </div>
      <div class="band band--bottom"></div>
    </section>

    <section class="card card--back" aria-label="Business card back">
      <div class="brand">
        <div class="brand-dot"></div>
        <div class="brand-name">Velmont Systems</div>
      </div>
      <div class="info-band">
        <div class="person">
          <div class="person-name">YOUR NAME</div>
          <div class="person-role">JOB NAME</div>
        </div>
        <div class="contact">
          <div>Phone:000.000.000 | Email:info@yourdomain.com</div>
          <div>www.yourwebsite.com | Adress Line 1</div>
          <div>Adress Line 2</div>
        </div>
      </div>
    </section>
  </main>
</body>
</html>
```